I need a new business card design for my pharmacy.

I need a business card design. I will include my logo.
The card needs to be readable. I prefer to have my logo on one side along with my website, the other side includes the other information. Please use combination of black, neon green, white, and silver. This needs to catch the eye but yet be clearly visible and legible. Thanks

Industry/Entity Type

Pharmacy

Contact Information for Business Card

It needs to have the following information listed:
Mel's Apothecary Owner/Pharm D.
7134 North Brook Lane
Cedarbrook, MN 55990
Phone 555-318-6207
Fax 555-318-6209
email: mel@melsapothecary-example.com
www.melsapothecary-example.com
Store hours Monday-Friday 8 am- 7 pm
Saturday 8 am- 12 pm
Sunday Closed
Please utilize the colors black, white, and neon green, maybe silver.

Requirements
Must have
• It needs to be easily readable!
Nice to have
• It should catch the eye.
Should not have
• Do not use any other colors except listed: black, neon green, white, & silver.

```html
<!DOCTYPE html>
<html lang="en">
<head>
<meta charset="utf-8">
<title>Mel's Apothecary – Business Card</title>
<link rel="stylesheet" href="https://fonts.googleapis.com/css2?family=Source+Sans+3:wght@400;600;700&family=Roboto+Condensed:wght@700&family=Source+Serif+4:wght@400&display=swap">
<style>
  :root {
    --ink: #161616;
    --white: #ffffff;
    --silver-light: #f4f4f4;
    --silver-mid: #d6d6d6;
    --silver-dark: #b4b4b4;
    --neon: #8dc63f;
    --backdrop: #e9e9e9;
  }
  * { margin: 0; padding: 0; box-sizing: border-box; }
  html, body { width: 1200px; height: 960px; overflow: hidden; }
  body {
    background: var(--backdrop);
    font-family: "Source Sans 3", Arial, sans-serif;
    color: var(--ink);
    position: relative;
  }
  .card {
    position: absolute;
    left: 257px;
    width: 688px;
    height: 416px;
    overflow: hidden;
  }
  .card--front { top: 42px; }
  .card--back { top: 502px; }
  .card__texture {
    position: absolute; inset: 0;
    background: linear-gradient(135deg, var(--silver-mid) 0%, var(--silver-light) 30%, var(--silver-dark) 55%, var(--silver-light) 80%, var(--silver-mid) 100%);
  }
  .brand {
    position: absolute;
    left: 44px; top: 142px;
    display: flex; align-items: center; gap: 22px;
  }
  .brand__dot {
    width: 58px; height: 58px; border-radius: 50%;
    background: var(--neon);
  }
  .brand__name {
    font-weight: 700;
    font-size: 56px;
    letter-spacing: -1.5px;
    line-height: 1;
    white-space: nowrap;
  }
  .website {
    position: absolute;
    left: 0; right: 0; top: 255px;
    text-align: center;
    font-family: "Roboto Condensed", "Arial Narrow", sans-serif;
    font-weight: 700;
    font-size: 31px;
    letter-spacing: 0.5px;
    white-space: nowrap;
  }
  .info-panel {
    position: absolute;
    left: 151px; top: 0;
    width: 410px; height: 100%;
    background: var(--white);
  }
  .info-list { list-style: none; }
  .info-item {
    position: absolute;
    left: 28px;
    display: flex; align-items: flex-start; gap: 22px;
    font-size: 18px; line-height: 23px;
    white-space: nowrap;
  }
  .info-icon {
    width: 33px; height: 33px; flex: none;
    border-radius: 50%; background: var(--ink);
    display: flex; align-items: center; justify-content: center;
    margin-top: -6px;
  }
  .info-icon svg { width: 17px; height: 17px; }
  .hours-title { font-family: "Source Serif 4", Georgia, serif; }
</style>
</head>
<body>

<section class="card card--front">
  <div class="card__texture" role="img" aria-label="Silver quilted diamond background pattern"></div>
  <div class="brand">
    <span class="brand__dot"></span>
    <span class="brand__name">Mel's Apothecary</span>
  </div>
  <p class="website">www.melsapothecary-example.com</p>
</section>

<section class="card card--back">
  <div class="card__texture" role="img" aria-label="Silver quilted diamond background pattern"></div>
  <div class="info-panel">
    <ul class="info-list">
      <li class="info-item" style="top:62px">
        <span class="info-icon"><svg viewBox="0 0 20 20" fill="#fff"><circle cx="10" cy="3" r="2"/><rect x="7.5" y="6" width="5" height="7" rx="1"/><rect x="8" y="12" width="1.6" height="6"/><rect x="10.4" y="12" width="1.6" height="6"/></svg></span>
        <span>Mel's Apothecary Owner/Pharm D.</span>
      </li>
      <li class="info-item" style="top:108px">
        <span class="info-icon"><svg viewBox="0 0 20 20" fill="none" stroke="#fff" stroke-width="1.8"><path d="M3 10 L10 3 L17 10"/><path d="M5 9 V17 H15 V9"/><rect x="8.5" y="12" width="3" height="5"/></svg></span>
        <span>7134 North Brook Lane<br>Cedarbrook, MN 55990</span>
      </li>
      <li class="info-item" style="top:177px">
        <span class="info-icon"><svg viewBox="0 0 20 20" fill="#fff"><path d="M5 2 L8 2 L9 6 L7 8 Q9 12 12 13 L14 11 L18 12 L18 15 Q17 18 14 18 Q4 16 2 6 Q2 3 5 2Z"/></svg></span>
        <span>Phone 555-318-6207</span>
      </li>
      <li class="info-item" style="top:223px">
        <span class="info-icon"><svg viewBox="0 0 20 20" fill="none" stroke="#fff" stroke-width="1.6"><rect x="6" y="2" width="8" height="5"/><rect x="2" y="7" width="16" height="7" rx="1.5"/><rect x="6" y="11" width="8" height="7" fill="#161616"/></svg></span>
        <span>Fax 555-318-6209</span>
      </li>
      <li class="info-item" style="top:269px">
        <span class="info-icon"><svg viewBox="0 0 20 20" fill="none" stroke="#fff" stroke-width="1.4"><rect x="2" y="4.5" width="16" height="11"/><path d="M2 4.5 L10 11 L18 4.5 M2 15.5 L8 9.5 M18 15.5 L12 9.5"/></svg></span>
        <span>email: mel@melsapothecary-example.com</span>
      </li>
      <li class="info-item" style="top:315px">
        <span class="info-icon"><svg viewBox="0 0 20 20" fill="none" stroke="#fff" stroke-width="1.6"><path d="M1.5 3 H4 L6 13 H16 L18 6 H5"/><circle cx="7.5" cy="16.5" r="1.3" fill="#fff"/><circle cx="14.5" cy="16.5" r="1.3" fill="#fff"/></svg></span>
        <span><span class="hours-title">Store hours</span><br>Monday-Friday 8 am- 7 pm<br>Saturday 8 am- 12 pm<br>Sunday Closed</span>
      </li>
    </ul>
  </div>
</section>

</body>
</html>
```